PulseLedgerPro.Com PowerPoint

I need a PowerPoint layout for my presentations. My business is called PulseLedgerPro.Com - my presentations teach cardiologists how to document their procedures and visits and teaches them how to bill accurately for them.

Industry/Entity Type

Business

Requirements
Must have
• the logo should be subtly there on each page - perhaps as a watermark? I'm really not creative; please help.

```html
<!DOCTYPE html>
<html lang="en">
<head>
<meta charset="utf-8">
<title>PulseLedgerPro.Com – Slide Layout</title>
<link rel="stylesheet" href="https://fonts.googleapis.com/css2?family=Graduate&family=Oswald:wght@600&family=Source+Sans+3:wght@400;600&display=swap">
<style>
  :root {
    --canvas: #ffffff;
    --slide-light: #efefef;
    --slide-mid: #dadada;
    --slide-shade: #cfcfcf;
    --charcoal: #212121;
    --brand-red: #be1e2d;
    --deep-red: #8a2a35;
    --tile-light: #29abe2;
    --tile-deep: #0b6fb8;
    --white: #ffffff;
  }
  * { margin: 0; padding: 0; box-sizing: border-box; }
  html, body {
    width: 1200px; height: 900px; overflow: hidden;
    background: var(--canvas);
  }
  .canvas { position: relative; width: 1200px; height: 900px; }

  .template-icon {
    position: absolute; left: 17px; top: 8px; width: 141px; height: 141px;
    background: linear-gradient(135deg, var(--tile-light) 45%, var(--tile-deep) 100%);
  }

  .slide {
    position: absolute; left: 35px; top: 171px; width: 1130px; height: 636px;
    background:
      linear-gradient(100deg, transparent 40%, rgba(255,255,255,0.35) 55%, transparent 70%),
      radial-gradient(ellipse at 62% 35%, var(--slide-light), var(--slide-mid) 70%, var(--slide-shade) 100%);
  }

  .image-frame {
    position: absolute; left: 29px; top: 34px; width: 470px; height: 416px;
    background: var(--charcoal);
  }
  .image-placeholder {
    position: absolute; left: 11px; top: 13px; width: 391px; height: 390px;
    background: linear-gradient(135deg, var(--brand-red) 48%, var(--deep-red) 52%, var(--deep-red) 100%);
  }
  .image-caption {
    position: absolute; left: 436px; top: 208px;
    transform: translate(-50%, -50%) rotate(-90deg);
    white-space: nowrap;
    font-family: "Source Sans 3", sans-serif; font-size: 26px;
    color: var(--white);
  }

  .slide-number {
    position: absolute; right: 15px; top: 13px; width: 100px; height: 100px;
  }
  .slide-number span {
    position: absolute; right: 12px; top: 16px;
    font-family: "Oswald", sans-serif; font-weight: 600; font-size: 22px;
    color: var(--white); line-height: 1;
  }

  .title-band {
    position: absolute; left: 16px; top: 484px; width: 1099px; height: 140px;
    background: var(--charcoal);
  }
  .slide-title {
    position: absolute; left: 24px; top: 20px; width: 412px;
    font-family: "Graduate", serif; font-weight: 400; font-size: 67px; line-height: 1;
    color: var(--brand-red); letter-spacing: 0; white-space: nowrap;
  }
  .title-rule {
    position: absolute; left: 24px; top: 87px; width: 412px; height: 3px;
    background: var(--white);
  }
  .slide-details {
    position: absolute; left: 79px; top: 100px;
    font-family: "Source Sans 3", sans-serif; font-size: 20px; letter-spacing: 0.4px;
    color: var(--white); text-transform: uppercase; white-space: nowrap;
  }

  .brand-mark {
    position: absolute; right: 14px; bottom: 12px;
    display: flex; align-items: center; gap: 7px;
    font-family: "Source Sans 3", sans-serif; font-weight: 600; font-size: 16px;
    color: var(--white);
  }
  .brand-mark .dot {
    width: 18px; height: 18px; border-radius: 50%; background: var(--brand-red);
  }
</style>
</head>
<body>
<div class="canvas">
  <div class="template-icon" role="img" aria-label="Template icon illustration"></div>

  <section class="slide">
    <div class="image-frame">
      <div class="image-placeholder" role="img" aria-label="Slide image placeholder"></div>
      <p class="image-caption">sample image placement</p>
    </div>

    <div class="slide-number">
      <svg width="100" height="100" viewBox="0 0 100 100" aria-hidden="true">
        <polygon points="0,0 100,0 100,100" fill="var(--brand-red)"/>
      </svg>
      <span>02</span>
    </div>

    <div class="title-band">
      <h1 class="slide-title">SLIDE TITLE</h1>
      <div class="title-rule"></div>
      <p class="slide-details">Details of slide / name of presentor</p>
      <div class="brand-mark"><span class="dot"></span>PulseLedgerPro.Com</div>
    </div>
  </section>
</div>
</body>
</html>
```